quarry productions business cards design

design a clean look but creative business card for a production company, I'm a freelance producer and launching my startup, would like to keep a clean professional look but still creative

Target Market(s)

businesses

Industry/Entity Type

video production

Contact Information for Business Card

logo, name (Karl Benn), Title (Producer), (MFA Filmmaking, QTSA Los Angeles), contact number & email ID

Colors

Designer to choose only greyscale colors for use in the design.

Requirements
Must have
• logo, black and white colors, you can play with their shades
Nice to have
• a unique design, not necessarily a typical size card
Should not have
• too colorful or playful

```html
<!DOCTYPE html>
<html lang="en">
<head>
<meta charset="utf-8">
<title>Quarry Productions – Business Card</title>
<link href="https://fonts.googleapis.com/css2?family=Roboto:wght@400;500;700&display=swap" rel="stylesheet">
<style>
  :root {
    --backdrop: #b5b5b5;
    --card-dark: #333233;
    --pattern-dark: #2b2a2b;
    --pattern-light: #383738;
    --panel-light: #efeef2;
    --ink: #2a292b;
    --ink-soft: #3a393b;
    --name-muted: #8a898b;
    --white: #ffffff;
  }
  * { margin: 0; padding: 0; box-sizing: border-box; }
  html, body {
    width: 1200px; height: 900px; overflow: hidden;
    background: var(--backdrop);
    font-family: "Roboto", sans-serif;
  }
  .canvas { position: relative; width: 1200px; height: 900px; }

  .card {
    position: absolute; left: 363px; width: 475px; height: 271px;
    background: var(--card-dark);
  }
  .card--front { top: 145px; overflow: hidden; }
  .card--back { top: 484px; }

  .front-pattern {
    position: absolute; inset: 0;
    background: radial-gradient(ellipse at center, var(--pattern-light) 0%, var(--pattern-dark) 100%);
  }
  .front-name {
    position: absolute; left: 0; right: 0; top: 118px;
    text-align: center; color: var(--name-muted);
    font-weight: 500; font-size: 30px; letter-spacing: 0.5px;
  }
  .front-url {
    position: absolute; left: 0; right: 0; top: 221px;
    text-align: center; color: var(--white);
    font-size: 11px; font-weight: 400;
  }

  .back-panel {
    position: absolute; left: 9px; top: 9px; width: 457px; height: 252px;
    background: var(--panel-light); border-radius: 4px;
  }
  .corner-frame { position: absolute; inset: 0; }
  .back-name {
    position: absolute; left: 32px; top: 110px; width: 200px;
    text-align: center; color: var(--ink);
    font-weight: 500; font-size: 18px; letter-spacing: 0.3px;
  }
  .profile {
    position: absolute; left: 231px; top: 66px; color: var(--ink-soft);
  }
  .profile__name { font-size: 16px; font-weight: 700; line-height: 19px; color: var(--ink); }
  .profile__line { font-size: 11px; line-height: 13.6px; }
  .contacts {
    position: absolute; left: 231px; top: 147px; color: var(--ink-soft);
    list-style: none;
  }
  .contacts li {
    display: flex; align-items: center; gap: 8px;
    font-size: 11px; line-height: 13.8px;
  }
  .contacts svg { width: 9px; height: 9px; flex: none; }
</style>
</head>
<body>
<div class="canvas">

  <section class="card card--front">
    <div class="front-pattern" role="img" aria-label="Repeating pattern of small film camera icons in dark grey"></div>
    <div class="front-name">quarry productions</div>
    <div class="front-url">www.<strong>quarryproductions</strong>.com</div>
  </section>

  <section class="card card--back">
    <div class="back-panel">
      <svg class="corner-frame" viewBox="0 0 457 252" fill="none" stroke="var(--ink)" stroke-width="2.4">
        <path d="M33 10 H17 Q8 10 8 19 V38"/>
        <path d="M424 10 H440 Q449 10 449 19 V38"/>
        <path d="M33 242 H17 Q8 242 8 233 V214"/>
        <path d="M424 242 H440 Q449 242 449 233 V214"/>
      </svg>

      <div class="back-name">quarry productions</div>

      <div class="profile">
        <div class="profile__name">Karl Benn</div>
        <div class="profile__line">Producer</div>
        <div class="profile__line">MFA in Filmmaking</div>
        <div class="profile__line">QTSA, Los Angeles</div>
      </div>

      <ul class="contacts">
        <li>
          <svg viewBox="0 0 10 10" fill="var(--ink)"><path d="M2 0.5 L3.6 2.6 L2.7 3.6 Q3.8 5.8 6.3 7.2 L7.3 6.3 L9.5 7.9 L8.4 9.5 Q3.5 8.5 0.6 1.6 Z"/></svg>
          200.555.0147
        </li>
        <li>
          <svg viewBox="0 0 10 10" fill="none" stroke="var(--ink)" stroke-width="1.2"><rect x="0.8" y="2" width="8.4" height="6"/><path d="M0.8 2 L5 5.5 L9.2 2"/></svg>
          karlbenn@quarryproductions.com
        </li>
        <li>
          <svg viewBox="0 0 10 10" fill="none" stroke="var(--ink)" stroke-width="0.9"><circle cx="5" cy="5" r="4.3"/><ellipse cx="5" cy="5" rx="1.9" ry="4.3"/><path d="M0.7 5 H9.3 M1.4 2.8 H8.6 M1.4 7.2 H8.6"/></svg>
          www.quarryproductions.com
        </li>
      </ul>
    </div>
  </section>

</div>
</body>
</html>
```